Kova Festivals

We need a website that covers a website with reviews about different festivals all around the world. Should include a directory of festivals and artists as well as a nice overview of articles.

Should include
Homepage,
Directory over artists and a detail page for artists also linking them to
a directory over festivals and a detail page for each festival with different information boxes
A nice and clean article category view for possible use of sub categories from main article archive
A modern, clean and good article page

Target Market(s)

People from all over the world that travels to music festivals and enjoys to check information online and share good deals.

Industry/Entity Type

Festival

Requirements
Must have
• Review pages with boxes and spaces for information about festivals

```html
<!DOCTYPE html>
<html lang="en">
<head>
<meta charset="utf-8">
<title>Kova Festivals</title>
<link rel="stylesheet" href="https://fonts.googleapis.com/css2?family=PT+Sans:ital,wght@0,400;0,700;1,400&family=Noto+Serif:ital@1&display=swap">
<style>
:root{
  --orange:#f39a1e;
  --text:#555;
  --dark:#444;
  --rule:#4a4a4a;
  --icon:#3d3d3d;
  --panel:rgba(255,255,255,.9);
  --nav-border:#d6d6d6;
  --button:#4f7fa3;
}
*{box-sizing:border-box;margin:0;padding:0}
html,body{width:1200px;height:2228px;overflow:hidden}
body{
  position:relative;
  font-family:"PT Sans",sans-serif;
  color:var(--text);
  background:
    radial-gradient(ellipse 260px 700px at 1120px 250px,rgba(240,225,120,.85),transparent),
    radial-gradient(ellipse 300px 800px at 300px 250px,rgba(140,100,170,.8),transparent),
    radial-gradient(ellipse 260px 900px at 900px 1000px,rgba(200,140,190,.6),transparent),
    radial-gradient(ellipse 250px 700px at 40px 1500px,rgba(140,170,110,.75),transparent),
    radial-gradient(ellipse 250px 700px at 1180px 1700px,rgba(240,210,110,.75),transparent),
    radial-gradient(ellipse 500px 300px at 600px 2180px,rgba(220,180,90,.7),transparent),
    linear-gradient(95deg,#b8a0c8,#e5d2a0 35%,#d9b0c8 65%,#e8d69a);
}
.brand{position:absolute;left:34px;top:45px;display:flex;align-items:center;gap:14px}
.brand-dot{width:46px;height:46px;border-radius:50%;background:var(--orange)}
.brand-name{font-size:34px;font-weight:700;color:var(--orange);letter-spacing:1px}
.social{position:absolute;left:918px;top:74px;display:flex;gap:5px}
.social span{width:28px;height:28px;border-radius:50%;border:2px solid #fff;box-shadow:0 1px 2px rgba(0,0,0,.3)}
.nav{position:absolute;left:30px;top:137px;width:1140px;height:63px;background:rgba(255,255,255,.93);box-shadow:0 1px 3px rgba(0,0,0,.2);display:flex}
.nav a{display:flex;align-items:center;padding:0 36px;font-size:16px;color:var(--dark);text-decoration:none;border-right:1px solid var(--nav-border)}
.panel{position:absolute;left:30px;top:226px;width:1140px;height:1894px;background:var(--panel);box-shadow:0 1px 4px rgba(0,0,0,.2)}
.abs{position:absolute}
.slide{left:35px;top:35px;width:1071px;height:475px;background:linear-gradient(180deg,#6f8a5a 0%,#8aa86a 35%,#6e9a3e 65%,#5c8a2e 100%)}
.caption{position:absolute;left:12px;bottom:10px;background:rgba(255,255,255,.9);padding:6px 18px;font-size:15px;color:#333}
.pager{left:480px;top:524px;display:flex;align-items:center;gap:7px}
.pager .arrow{width:30px;height:30px;border-radius:50%;background:#4a4a4a;display:flex;align-items:center;justify-content:center}
.pager .dot{width:14px;height:14px;border-radius:50%;background:#4a4a4a}
.pager .dot.on{background:#fff;border:2px solid #4a4a4a}
.lead{left:50px;top:580px;width:1040px;text-align:center;font-family:"Noto Serif",serif;font-style:italic;font-size:22px;line-height:37px;color:#444}
.double-rule{left:35px;width:1071px;height:7px;border-top:3px solid var(--rule);border-bottom:1px solid var(--rule)}
.rule{left:35px;width:1071px;border-top:1px solid #777}
h2,h3{font-weight:400;color:var(--orange)}
h2{font-size:22px}
h3{font-size:19px}
.body-text{font-size:15.5px;line-height:24px;color:#555}
.checklist{list-style:none;font-family:"Noto Serif",serif;font-style:italic;font-size:14.5px;line-height:24px;color:#444}
.checklist li::before{content:"›";font-style:normal;margin-right:14px}
.services{left:35px;top:935px;width:1071px;display:flex;justify-content:space-between}
.service{width:225px;text-align:center}
.service svg{display:block;margin:0 auto 22px;height:58px}
.service h3{margin-bottom:12px}
.service p{font-size:15.5px;line-height:24px}
.works-nav{left:1048px;top:1203px;display:flex;gap:6px}
.works-nav span{width:26px;height:26px;border-radius:50%;background:#4a4a4a;display:flex;align-items:center;justify-content:center}
.works{left:35px;top:1253px;display:flex;gap:24px}
.works div{width:195px;height:156px}
.col{top:1508px;width:235px}
.col h3{margin-bottom:20px}
.post{display:flex;gap:14px;padding:6px 0 10px;border-bottom:2px dashed #666;margin-bottom:8px;width:235px}
.post:last-child{border-bottom:none}
.post .date{width:38px;text-align:center;font-family:"Noto Serif",serif;font-style:italic;color:#333}
.post .date b{display:block;font-weight:400;font-size:26px;line-height:28px}
.post .date i{display:block;font-size:13px;line-height:14px}
.post p{width:175px;font-size:15.5px;line-height:24px}
.gallery{display:grid;grid-template-columns:repeat(3,69px);gap:14px}
.gallery div{height:69px}
.col.about p{margin-bottom:16px;font-size:15.5px;line-height:24px}
.field{display:flex;align-items:center;gap:10px;margin-bottom:14px;font-size:13px;color:#444}
.field span{width:181px;height:37px;border:1px solid #ccc;border-radius:4px;background:#fff}
.message{width:236px;height:155px;border:1px solid #ccc;border-radius:4px;background:#fff;margin-bottom:14px}
.submit{width:100px;height:31px;background:var(--button);color:#fff;font-family:"Noto Serif",serif;font-style:italic;font-size:15px;display:flex;align-items:center;justify-content:center}
.footer{position:absolute;left:30px;top:2144px;width:1140px;height:68px;background:rgba(255,255,255,.9);display:flex;align-items:center;justify-content:center;font-size:13px;color:#444}
</style>
</head>
<body>
<header>
  <div class="brand"><span class="brand-dot"></span><span class="brand-name">Kova Festivals</span></div>
  <div class="social" aria-label="Social links">
    <span style="background:#f1902c"></span><span style="background:#3b5b98"></span><span style="background:#33b5e6"></span><span style="background:#333"></span><span style="background:#e34c8e"></span><span style="background:#d8d8d8"></span><span style="background:#4d6d8e"></span>
  </div>
  <nav class="nav">
    <a href="#">Home</a><a href="#">Festivals</a><a href="#">Artists</a><a href="#">Reviews</a><a href="#">Articles</a><a href="#">Contact</a>
  </nav>
</header>

<main class="panel">
  <div class="abs slide" role="img" aria-label="Photo of families playing games on the lawn at an outdoor festival">
    <div class="caption">Summer Fields review: three days of sun, bass and dancing on the lawn.</div>
  </div>
  <div class="abs pager">
    <span class="arrow"><svg width="10" height="12" viewBox="0 0 10 12"><path d="M7 1 2 6l5 5" stroke="#fff" stroke-width="1.6" fill="none"/></svg></span>
    <span class="dot"></span><span class="dot"></span><span class="dot"></span><span class="dot"></span><span class="dot on"></span>
    <span class="arrow"><svg width="10" height="12" viewBox="0 0 10 12"><path d="M3 1l5 5-5 5" stroke="#fff" stroke-width="1.6" fill="none"/></svg></span>
  </div>
  <p class="abs lead">Honest reviews of music festivals all around the world, with line-ups, artists and travel tips. Find your next festival weekend and share the best deals.</p>

  <div class="abs double-rule" style="top:694px"></div>

  <h2 class="abs" style="left:35px;top:746px">What We Cover</h2>
  <p class="abs body-text" style="left:35px;top:786px;width:700px">Kova Festivals is a guide for travellers who follow the music. Every festival page brings the line-up, dates, tickets, camping and travel facts together in clear information boxes. Our reviewers rate sound, stages, food and crowd, and the artist directory links each act to every festival where you can see them play.</p>
  <ul class="abs checklist" style="left:775px;top:788px">
    <li>Ratings for sound, stage and camping.</li>
    <li>Line-ups linked to artist pages.</li>
    <li>Ticket prices and travel deals.</li>
    <li>Articles sorted by region and genre.</li>
  </ul>

  <section class="abs services">
    <div class="service">
      <svg viewBox="0 0 56 56" width="56"><path d="M28 3l7.6 15.4 17 2.5-12.3 12 2.9 16.9L28 41.8l-15.2 8 2.9-16.9-12.3-12 17-2.5z" fill="var(--icon)"/></svg>
      <h3>Festival Reviews</h3><p>Scores and honest notes on sound, stages, food and the crowd at every event.</p>
    </div>
    <div class="service">
      <svg viewBox="0 0 56 56" width="56"><rect x="19" y="2" width="18" height="30" rx="9" fill="var(--icon)"/><path d="M12 24a16 16 0 0 0 32 0" stroke="var(--icon)" stroke-width="3" fill="none"/><rect x="26" y="40" width="4" height="10" fill="var(--icon)"/><rect x="16" y="50" width="24" height="4" fill="var(--icon)"/></svg>
      <h3>Artist Directory</h3><p>Every act with a short profile and links to the festivals where they play.</p>
    </div>
    <div class="service">
      <svg viewBox="0 0 56 56" width="56"><path d="M28 2a18 18 0 0 0-18 18c0 14 18 34 18 34s18-20 18-34A18 18 0 0 0 28 2z" fill="var(--icon)"/><circle cx="28" cy="20" r="7" fill="#fff"/></svg>
      <h3>Festival Guide</h3><p>Dates, tickets, camping and travel facts in clear boxes for each festival.</p>
    </div>
    <div class="service">
      <svg viewBox="0 0 56 56" width="56"><path d="M4 6h22l26 26-20 20L6 26z" fill="var(--icon)"/><circle cx="16" cy="16" r="4" fill="#fff"/></svg>
      <h3>Travel Deals</h3><p>Ticket offers, cheap flights and shared rides posted by fellow fans.</p>
    </div>
  </section>

  <div class="abs rule" style="top:1163px"></div>

  <h2 class="abs" style="left:35px;top:1205px">Latest Reviews</h2>
  <div class="abs works-nav">
    <span><svg width="8" height="10" viewBox="0 0 8 10"><path d="M6 1 2 5l4 4" stroke="#fff" stroke-width="1.5" fill="none"/></svg></span>
    <span><svg width="8" height="10" viewBox="0 0 8 10"><path d="M2 1l4 4-4 4" stroke="#fff" stroke-width="1.5" fill="none"/></svg></span>
  </div>
  <div class="abs works">
    <div role="img" aria-label="Festival parade float covered in flowers" style="background:linear-gradient(160deg,#9cc46a,#d8b040 50%,#8a8a7a)"></div>
    <div role="img" aria-label="Street dancers in red costumes" style="background:linear-gradient(180deg,#c9c3b6,#b5483a 60%,#8c8070)"></div>
    <div role="img" aria-label="Performers in costume on a decorated stage" style="background:linear-gradient(160deg,#d8b84a,#7a4a8a 55%,#c85a3a)"></div>
    <div role="img" aria-label="Parade performers under festival banners" style="background:linear-gradient(180deg,#d8d0c8,#b03a2a 55%,#6a6a70)"></div>
    <div role="img" aria-label="Colourful costumed dance troupe" style="background:linear-gradient(160deg,#4a8a5a,#3a5aa8 50%,#e0c040)"></div>
  </div>

  <div class="abs double-rule" style="top:1460px"></div>

  <section class="abs col" style="left:35px">
    <h3>Latest Articles</h3>
    <div class="post"><div class="date"><b>22</b><i>JUN</i></div><p>Ten summer festivals worth a flight</p></div>
    <div class="post"><div class="date"><b>14</b><i>MAY</i></div><p>How to camp light at a big festival</p></div>
    <div class="post"><div class="date"><b>11</b><i>MAY</i></div><p>New artists to catch on tour this year</p></div>
    <div class="post"><div class="date"><b>08</b><i>APR</i></div><p>Early bird tickets: our best deals</p></div>
  </section>

  <section class="abs col" style="left:313px">
    <h3>Gallery</h3>
    <div class="gallery">
      <div role="img" aria-label="Festival photo" style="background:linear-gradient(135deg,#c8c0a8,#8a9a6a)"></div>
      <div role="img" aria-label="Festival photo" style="background:linear-gradient(135deg,#e8e0d0,#b89a78)"></div>
      <div role="img" aria-label="Festival photo" style="background:linear-gradient(135deg,#e8dcd4,#c8a89a)"></div>
      <div role="img" aria-label="Festival photo" style="background:linear-gradient(135deg,#f0e4dc,#c89a88)"></div>
      <div role="img" aria-label="Festival photo" style="background:linear-gradient(135deg,#b8b098,#7a8a5a)"></div>
      <div role="img" aria-label="Festival photo" style="background:linear-gradient(135deg,#eeeeea,#6a9a4a)"></div>
      <div role="img" aria-label="Festival photo" style="background:linear-gradient(135deg,#e8e4dc,#c86a4a)"></div>
      <div role="img" aria-label="Festival photo" style="background:linear-gradient(135deg,#d8e4ec,#3a8ac8)"></div>
      <div role="img" aria-label="Festival photo" style="background:linear-gradient(135deg,#f0ece4,#b8a890)"></div>
    </div>
  </section>

  <section class="abs col about" style="left:592px">
    <h3>About</h3>
    <p>Kova Festivals is run by fans who travel the world for live music. We visit each festival, rate it fairly and keep the facts up to date for you.</p>
    <p>Found a good deal or a great new festival? Tell us and share it.</p>
  </section>

  <section class="abs col" style="left:870px;width:260px">
    <h3>Get in Touch</h3>
    <div class="field"><span></span>Name*</div>
    <div class="field"><span></span>Email*</div>
    <div class="message"></div>
    <div class="submit">Submit</div>
  </section>
</main>

<footer class="footer">© 2013 Kova Festivals. All Right Reserved.</footer>
</body>
</html>
```